Stationery Design Project

Hi All,

We need you to design stationary for a new Business and Accounting Advisory Firm. We have already got the logo designed and it is attached. If you could also if possible, match the fonts in your design to that on the logo’s provided.

What we need:
- Business Card
- A4 Letter head
- A4 Folders
- PPT template (Title page and regular page)

And what ever else you want to throw in.

We are in the process of getting the web site designed, however below is a list of websites which we like which will give you an understanding of the style that we are going for.

- plavoni.com
- brightfunnelo.com
- hourquillet.com
- artmarrowly.com

I look forward to your seeing your design.

Hi All,

I have just realised that I forgot that i need to include a Licensed Tallymasters image on the letter head, please find attaced as File 1. Could you please have this image in the bottom left header.

Regards,

Gareth

Industry/Entity Type

Business

Requirements
Must have
• Outputs:
- Documents ready to print
- Generic editable information
- Pdf copies of the documents
- Word version of letterhead

```html
<!DOCTYPE html>
<html lang="en">
<head>
<meta charset="utf-8">
<title>Brenwick Partners – Stationery Set</title>
<link rel="stylesheet" href="https://fonts.googleapis.com/css2?family=Crimson+Text:wght@400;600&family=Arimo:wght@400;700&display=swap">
<style>
  :root{
    --navy:#2f4f8f;
    --blue:#3a7fbf;
    --cyan:#46c3dc;
    --yellow:#fdcb3a;
    --orange:#f4822a;
    --ink:#2f4a8c;
    --paper:#ffffff;
    --stage:#eceef1;
    --line:#d5d8dc;
    --badge:#c8262c;
    --serif:"Crimson Text", Georgia, serif;
    --sans:"Arimo", Arial, sans-serif;
  }
  *{box-sizing:border-box;margin:0;padding:0}
  html,body{width:1200px;height:900px;overflow:hidden}
  body{position:relative;background:var(--paper);font-family:var(--sans);color:var(--ink)}
  .stage{position:absolute;left:0;top:0;width:752px;height:900px;background:var(--stage)}
  .sheet{position:absolute;background:var(--paper);border:1px solid var(--line);overflow:hidden}

  .brand{font-family:var(--serif);color:var(--ink);line-height:1}
  .brand__name{font-weight:400;display:block}
  .brand__tag{display:block;font-family:var(--sans);letter-spacing:.32em;color:var(--ink)}
  .mark{display:inline-block;background:var(--paper)}

  .band-blue{background:linear-gradient(90deg,var(--navy),var(--blue) 45%,var(--cyan))}
  .band-warm{background:linear-gradient(90deg,var(--yellow),var(--orange))}
  .band-cyan{background:var(--cyan)}
  .band-yellow{background:var(--yellow)}

  .contact{font-size:7px;line-height:1.45;color:var(--ink);font-weight:700}
  .contact span{display:inline-block;width:12px;font-weight:400}

  .web{font-size:8px;letter-spacing:.3em;color:#fff}

  /* folder */
  .folder{left:40px;top:70px;width:330px;height:460px}
  .folder__top{position:absolute;left:0;top:0;right:0;height:52px}
  .folder__brand{position:absolute;left:34px;top:82px}
  .folder__brand .brand__name{font-size:27px}
  .folder__brand .brand__tag{font-size:8.5px;margin-top:4px}
  .folder__contact{position:absolute;left:34px;top:330px}
  .folder__foot{position:absolute;left:0;right:0;bottom:0;height:72px;display:flex;align-items:center;gap:14px;padding-left:34px}
  .folder__foot .mark{width:26px;height:26px;border-radius:50%}

  /* letterhead */
  .letterhead{left:400px;top:70px;width:318px;height:450px}
  .letterhead__brand{position:absolute;left:22px;top:22px}
  .letterhead__brand .brand__name{font-size:18px}
  .letterhead__brand .brand__tag{font-size:6px;margin-top:3px}
  .letterhead__address{position:absolute;right:18px;top:24px;text-align:right;font-size:6.5px;line-height:1.5;font-weight:700;font-style:italic}
  .letterhead__curve{position:absolute;left:0;top:40px;width:318px;height:60px}
  .letterhead__badge{position:absolute;left:22px;bottom:58px;display:flex;align-items:center;gap:8px;font-size:8px;font-weight:700;color:#222;line-height:1.1}
  .letterhead__badge i{width:20px;height:20px;border-radius:50%;background:var(--badge);display:block}
  .letterhead__rule{position:absolute;left:140px;right:0;bottom:28px;height:6px}
  .letterhead__web{position:absolute;left:150px;bottom:38px;font-size:7px;letter-spacing:.3em;color:var(--yellow)}

  /* business cards */
  .card{top:77px;width:176px;height:113px}
  .card--front{left:786px}
  .card--back{left:989px}
  .card__top{position:absolute;left:0;right:0;top:0;height:19px}
  .card__bottom{position:absolute;left:0;right:0;bottom:0;height:20px}
  .card--front .brand{position:absolute;left:14px;top:45px}
  .card--front .brand__name{font-size:15px}
  .card--front .brand__tag{font-size:5px;margin-top:2px}
  .card__tagline{position:absolute;right:8px;top:6px;font-size:6px;letter-spacing:.3em;color:#fff}
  .card__person{position:absolute;right:9px;top:24px;text-align:right}
  .card__name{font-family:var(--serif);font-weight:600;font-size:10px}
  .card__role{font-size:5px;font-weight:700;margin-top:2px}
  .card--back .contact{position:absolute;left:12px;top:56px;font-size:5px}
  .card--back .contact span{width:9px}
  .card__bottom--back{display:flex;align-items:center;justify-content:space-between;padding:0 10px 0 14px}
  .card__bottom--back .mark{width:13px;height:13px;border-radius:50%}
  .card__bottom--back .web{font-size:5.5px}

  /* slides */
  .slide{left:786px;width:379px;height:285px}
  .slide--title{top:263px}
  .slide--content{top:570px}
  .slide--title .slide__top{position:absolute;left:0;right:0;top:0;height:24px}
  .slide--title .brand{position:absolute;left:0;right:0;top:43px;text-align:center}
  .slide--title .brand__name{font-size:24px}
  .slide--title .brand__tag{font-size:7px;margin-top:3px;padding-left:60px}
  .slide__heading{position:absolute;left:0;right:0;top:160px;text-align:center;font-family:var(--serif);font-weight:400;font-size:23px;letter-spacing:.12em;color:var(--ink)}
  .slide--title .slide__foot{position:absolute;left:0;right:0;bottom:0;height:74px;display:flex;align-items:center;justify-content:center}
  .slide--content .slide__top{position:absolute;left:0;right:0;top:0;height:20px;display:flex;align-items:center;padding-left:16px;font-size:7.5px;letter-spacing:.28em;color:#fff}
  .slide--content .slide__foot{position:absolute;left:0;right:0;bottom:0;height:22px;display:flex;align-items:center;justify-content:space-between;padding:0 14px 0 16px}
  .slide--content .slide__foot .mark{width:14px;height:14px;border-radius:50%}
  .slide--content .web{font-size:7px}
</style>
</head>
<body>
  <div class="stage"></div>

  <!-- A4 folder, front cover -->
  <section class="sheet folder" aria-label="Folder front">
    <div class="folder__top band-blue"></div>
    <div class="brand folder__brand">
      <span class="brand__name">Brenwick Partners</span>
      <span class="brand__tag">Business Advisors</span>
    </div>
    <div class="contact folder__contact">
      <div><span>A:</span>12 Mill Road, Harbourton</div>
      <div><span>T:</span>000 000 0000 &nbsp; F: 000 000 0001</div>
      <div><span>M:</span>000 000 0002</div>
      <div><span>E:</span>hello@brenwick.com</div>
    </div>
    <div class="folder__foot band-warm">
      <i class="mark"></i>
      <span class="web">www.brenwickpartners.com</span>
    </div>
  </section>

  <!-- A4 letterhead -->
  <section class="sheet letterhead" aria-label="Letterhead">
    <div class="brand letterhead__brand">
      <span class="brand__name">Brenwick Partners</span>
      <span class="brand__tag">Business Advisors</span>
    </div>
    <div class="letterhead__address">
      12 Mill Road, Harbourton,<br>Westvale 0000<br>T: 000 000 0000, F: 000 000 0001
    </div>
    <svg class="letterhead__curve" viewBox="0 0 318 60" aria-hidden="true">
      <path d="M0 30 C90 34 150 46 210 38 C255 32 290 44 318 50" fill="none" stroke="var(--cyan)" stroke-width="5"/>
    </svg>
    <div class="letterhead__badge"><i></i><span>Licensed<br>Tallymaster</span></div>
    <div class="letterhead__web">www.brenwickpartners.com</div>
    <div class="letterhead__rule band-yellow"></div>
  </section>

  <!-- Business card, front -->
  <section class="sheet card card--front" aria-label="Business card front">
    <div class="card__top band-cyan"></div>
    <div class="brand">
      <span class="brand__name">Brenwick Partners</span>
      <span class="brand__tag">Business Advisors</span>
    </div>
    <div class="card__bottom band-yellow"></div>
  </section>

  <!-- Business card, back -->
  <section class="sheet card card--back" aria-label="Business card back">
    <div class="card__top band-cyan"><span class="card__tagline">Business Advisors</span></div>
    <div class="card__person">
      <div class="card__name">Firstname Lastname</div>
      <div class="card__role">Position position</div>
    </div>
    <div class="contact">
      <div><span>A:</span>12 Mill Road, Harbourton</div>
      <div><span>T:</span>000 000 0000 &nbsp; F: 000 000 0001</div>
      <div><span>M:</span>000 000 0002</div>
      <div><span>E:</span>hello@brenwick.com</div>
    </div>
    <div class="card__bottom card__bottom--back band-yellow">
      <i class="mark"></i>
      <span class="web">www.brenwickpartners.com</span>
    </div>
  </section>

  <!-- Presentation, title slide -->
  <section class="sheet slide slide--title" aria-label="Presentation title slide">
    <div class="slide__top band-blue"></div>
    <div class="brand">
      <span class="brand__name">Brenwick Partners</span>
      <span class="brand__tag">Business Advisors</span>
    </div>
    <h1 class="slide__heading">Presentation name</h1>
    <div class="slide__foot band-warm"><span class="web">www.brenwickpartners.com</span></div>
  </section>

  <!-- Presentation, content slide -->
  <section class="sheet slide slide--content" aria-label="Presentation content slide">
    <div class="slide__top band-blue">Presentation name</div>
    <div class="slide__foot band-warm">
      <i class="mark"></i>
      <span class="web">www.brenwickpartners.com</span>
    </div>
  </section>
</body>
</html>
```